I need a website designed. I am a mortgage loan officer and would like to have a website for me and my team where i can post resources, videos and blog information for my clients. A website like thelorvikteam.com .

The theme is - The Pellam Team - Home Loan Group powered by Brightmoor Home Loans -

Target Market(s)

B2B (Real Estate Agents)and B2C (Home buyers and refinancing)

Industry/Entity Type

Mortgage Lender

Coding

Coded - Design and coding required

Number of Pages Required

5+ page

Font styles to use
Serif
Sans Serif

Colors

Designer to choose colors to be used in the design.

Requirements
Must have
• Disclaimers: Licensed by the Office of Commerce Stewardship under the Westland Credit Providers Act. Loans made or arranged pursuant to a Westland Credit Providers Act License. Equal Housing Lender Brightmoor Cannot Accept mortgage applications for properties located in New York via this site
• Mobile Friendly
Nice to have
• Main Links: Home, About Us(see team flyer), Mortgage 101, Contact Us (formly form)

```html
<!DOCTYPE html>
<html lang="en">
<head>
<meta charset="utf-8">
<title>The Pellam Team – Home Loan Group</title>
<link href="https://fonts.googleapis.com/css2?family=Barlow:wght@400;500;600;700;800&display=swap" rel="stylesheet">
<style>
:root{
  --blue:#1f6dbf;
  --blue-dark:#17589e;
  --ink:#1d232b;
  --text:#3b4047;
  --muted:#8a9099;
  --gray:#ececec;
  --footer:#242b35;
  --footer-line:#3a4350;
  --white:#ffffff;
}
*{box-sizing:border-box;margin:0;padding:0}
html,body{width:1200px;height:3488px;overflow:hidden}
body{font-family:"Barlow",Arial,sans-serif;color:var(--text);background:var(--white);position:relative}
a{color:inherit;text-decoration:none}

/* header */
.site-header{position:absolute;top:0;left:0;width:1200px;height:121px;background:var(--white)}
.search{position:absolute;left:70px;top:10px;width:197px;height:30px;border:2px solid var(--blue);border-radius:15px;display:flex;align-items:center;justify-content:space-between;padding:0 12px;font-size:13px;font-weight:700;color:var(--ink)}
.topbar-contact{position:absolute;right:70px;top:14px;display:flex;gap:26px;font-size:13px;font-weight:600;color:var(--blue-dark)}
.topbar-contact span{display:flex;align-items:center;gap:6px}
.brand{position:absolute;left:470px;top:14px;width:260px;text-align:center}
.brand-mark{display:inline-block;width:26px;height:26px;background:var(--blue);margin-bottom:4px}
.brand-name{font-size:25px;font-weight:700;color:var(--blue);letter-spacing:.5px;line-height:1}
.brand-sub{font-size:13px;font-weight:500;color:var(--blue);letter-spacing:3px;margin-top:3px}
.main-nav a{position:absolute;top:76px;font-size:14px;font-weight:700;color:var(--ink);letter-spacing:.5px}
.main-nav a.active{color:var(--blue)}

/* hero */
.hero{position:absolute;top:121px;left:0;width:1200px;height:500px;background:linear-gradient(180deg,#8fb3d6 0%,#a7a29a 45%,#7b7670 75%,#9c958c 100%);text-align:center;color:var(--white)}
.hero h1{position:absolute;top:152px;width:100%;font-size:86px;font-weight:800;line-height:1;letter-spacing:1px}
.hero h2{position:absolute;top:242px;width:100%;font-size:52px;font-weight:700;line-height:1;letter-spacing:1px}
.btn{display:flex;align-items:center;justify-content:center;width:210px;height:52px;font-size:14px;font-weight:700;letter-spacing:1px}
.btn-hero{position:absolute;left:495px;top:332px;background:rgba(90,90,90,.75);color:var(--white)}

/* about */
.about{position:absolute;top:621px;left:0;width:1200px;height:444px;background:var(--blue);color:var(--white);text-align:center}
.section-title{font-size:32px;font-weight:700;letter-spacing:1px;line-height:1}
.title-rule{width:112px;height:4px;margin:14px auto 0;background:var(--muted)}
.about .section-title{padding-top:82px}
.about .title-rule{background:rgba(255,255,255,.55)}
.about p{width:600px;margin:36px auto 0;font-size:13.5px;line-height:19px}
.about p + p{margin-top:18px}
.btn-outline-light{position:absolute;left:495px;top:320px;border:2px solid var(--white);color:var(--white)}

/* videos */
.videos{position:absolute;top:1065px;left:0;width:1200px;height:570px;background:var(--white);text-align:center}
.videos .section-title,.blog .section-title,.team .section-title{color:var(--blue)}
.videos .section-title{padding-top:93px}
.card-row{position:absolute;left:67px;display:flex;gap:28px}
.video-row{top:210px}
.video-card{width:337px}
.thumb{position:relative;width:337px;height:239px}
.play{position:absolute;left:138px;top:89px;width:60px;height:60px;border-radius:50%;background:var(--blue);border:4px solid var(--white)}
.play::after{content:"";position:absolute;left:20px;top:14px;border-left:20px solid var(--white);border-top:12px solid transparent;border-bottom:12px solid transparent}
.video-card h3{margin-top:18px;font-size:14px;font-weight:700;color:var(--ink);letter-spacing:.3px}

/* team */
.team{position:absolute;top:1635px;left:0;width:1200px;height:731px;background:var(--gray);text-align:center}
.team .section-title{padding-top:93px}
.member{position:absolute;width:520px;height:178px;text-align:left}
.member .portrait{position:absolute;left:0;top:0;width:191px;height:177px}
.member .info{position:absolute;left:205px;top:0}
.member h3{font-size:19px;font-weight:700;color:var(--ink);line-height:1;letter-spacing:.3px}
.member .role{font-size:11.5px;font-weight:600;color:var(--text);margin-top:4px}
.member .rule{width:60px;height:1px;background:var(--muted);margin:10px 0 8px}
.member .details{font-size:11px;line-height:16px;color:var(--muted)}
.btn-small{display:flex;align-items:center;justify-content:center;width:106px;height:30px;border:1px solid var(--blue);background:var(--white);color:var(--ink);font-size:11px;font-weight:700;position:absolute;top:144px;left:205px}

/* blog */
.blog{position:absolute;top:2366px;left:0;width:1200px;height:739px;background:var(--white);text-align:center}
.blog .section-title{padding-top:56px}
.blog-row{top:151px}
.post{width:337px;text-align:left}
.post .thumb{height:237px}
.post h3{margin-top:29px;font-size:14px;font-weight:700;color:var(--ink);line-height:19px}
.post p{margin-top:18px;font-size:11.5px;line-height:16px;color:var(--muted)}
.post .rule{width:66px;height:1px;background:var(--ink);margin:20px 0 14px}
.post time{font-size:14px;font-weight:700;color:var(--blue)}
.btn-outline{position:absolute;left:495px;top:639px;border:2px solid var(--blue);color:var(--ink)}

/* footer */
.site-footer{position:absolute;top:3105px;left:0;width:1200px;height:383px;background:var(--footer);color:#c9ced6}
.footer-brand{position:absolute;left:95px;top:46px;text-align:center;width:190px}
.footer-brand .brand-name{font-size:22px}
.footer-brand .brand-sub{font-size:11px;letter-spacing:2.5px}
.footer-badges{position:absolute;left:100px;top:148px;display:flex;align-items:center;gap:14px}
.badge{width:38px;height:38px;background:#c9ced6}
.partner{display:flex;align-items:center;gap:8px;font-size:16px;font-weight:600;color:#c9ced6}
.partner i{width:20px;height:20px;background:#5b7fb0;display:block}
.footer-col{position:absolute;top:46px}
.footer-col h4{font-size:13px;font-weight:700;color:var(--blue);letter-spacing:.5px;margin-bottom:14px}
.footer-col li{list-style:none;font-size:12px;font-weight:600;line-height:25px;color:#dfe3e8}
.resources{left:796px;width:330px}
.resources .arrows{position:absolute;right:0;top:0;font-size:13px;color:var(--white)}
.resource{display:flex;gap:8px;font-size:11px;line-height:15px;color:var(--muted);margin-bottom:12px}
.resource span{color:var(--blue)}
.resource time{display:block;color:var(--blue);font-weight:700;font-size:12px;margin-top:3px}
.disclaimer{position:absolute;top:254px;left:80px;width:1040px;text-align:center}
.disclaimer h4{font-size:12px;font-weight:700;color:var(--blue);letter-spacing:.5px}
.disclaimer p{margin-top:16px;font-size:12.5px;line-height:18px;color:#b4bac3}
.copyright{position:absolute;top:346px;left:0;width:1200px;border-top:1px solid var(--footer-line);padding-top:10px;text-align:center;font-size:11px;font-weight:600;letter-spacing:.5px;color:#c9ced6}
</style>
</head>
<body>

<header class="site-header">
  <div class="search">SEARCH
    <svg width="14" height="14" viewBox="0 0 14 14"><circle cx="6" cy="6" r="4.2" fill="none" stroke="#1d232b" stroke-width="2"/><line x1="9" y1="9" x2="13" y2="13" stroke="#1d232b" stroke-width="2"/></svg>
  </div>
  <div class="topbar-contact">
    <span><svg width="10" height="13" viewBox="0 0 10 13"><path d="M5 0a5 5 0 0 0-5 5c0 3.5 5 8 5 8s5-4.5 5-8a5 5 0 0 0-5-5z" fill="#17589e"/><circle cx="5" cy="5" r="1.8" fill="#fff"/></svg>410 ELMSTEAD RD, SUITE 12, FAIRHAVEN FL 30010</span>
    <span><svg width="12" height="12" viewBox="0 0 12 12"><path d="M2.5 0l2 2.8-1.3 1.5a7 7 0 0 0 4.5 4.5l1.5-1.3L12 9.5 10.6 12C4.8 11.6.4 7.2 0 1.4z" fill="#17589e"/></svg>1-555-014-2290</span>
  </div>
  <div class="brand">
    <span class="brand-mark"></span>
    <div class="brand-name">THE PELLAM TEAM</div>
    <div class="brand-sub">HOME LOAN GROUP</div>
  </div>
  <nav class="main-nav">
    <a class="active" href="#" style="left:242px">HOME</a>
    <a href="#" style="left:332px">ABOUT US</a>
    <a href="#" style="left:726px">MORTGAGE 101</a>
    <a href="#" style="left:875px">CONTACT US</a>
  </nav>
</header>

<section class="hero" role="img" aria-label="Photo of a large two-storey family home behind an iron gate and paved driveway">
  <h1>THE PELLAM TEAM</h1>
  <h2>A HOME LOAN COMPANY</h2>
  <a class="btn btn-hero" href="#">LEARN MORE</a>
</section>

<section class="about">
  <h2 class="section-title">ABOUT US</h2>
  <div class="title-rule"></div>
  <p>Qui dolorem ipsum quia dolor sit amet, consectetur, adipisci velit, sed quia non numquam eius modi tempora incidunt ut labore et dolore magnam aliquam quaerat voluptatem.</p>
  <p>Ut enim ad minima veniam, quis nostrum exercitationem ullam corporis suscipit laboriosam, nisi ut aliquid ex ea commodi qui dolorem ipsum quia dolor sit amet, consectetur, adipisci velit, sed quia non numquam eius modi tempora.</p>
  <a class="btn btn-outline-light" href="#">READ MORE</a>
</section>

<section class="videos">
  <h2 class="section-title">VIDEOS</h2>
  <div class="title-rule"></div>
  <div class="card-row video-row">
    <article class="video-card">
      <div class="thumb" role="img" aria-label="Video still: couple touring a bright home interior with an agent" style="background:linear-gradient(135deg,#f1ece4,#cdb79a)"><span class="play"></span></div>
      <h3>QUIA DOLOR SIT AMET, CONSECTETU</h3>
    </article>
    <article class="video-card">
      <div class="thumb" role="img" aria-label="Video still: lit house with a wooden deck at dusk" style="background:linear-gradient(180deg,#3c4b60,#8a5a38)"><span class="play"></span></div>
      <h3>OCCAECATI CUPIDITATE NON PROVIDENT</h3>
    </article>
    <article class="video-card">
      <div class="thumb" role="img" aria-label="Video still: family relaxing on a porch railing" style="background:linear-gradient(135deg,#a8b69a,#6d5a44)"><span class="play"></span></div>
      <h3>POSSIMUS, OMNIS VOLUPTAS ASSUMENDA</h3>
    </article>
  </div>
</section>

<section class="team">
  <h2 class="section-title">OUR TEAM</h2>
  <div class="title-rule"></div>

  <article class="member" style="left:67px;top:205px">
    <div class="portrait" role="img" aria-label="Portrait of Marco Pellam" style="background:linear-gradient(180deg,#cfd3d8,#6f7378)"></div>
    <div class="info">
      <h3>MARCO PELLAM</h3>
      <div class="role">Producing Branch Manager</div>
      <div class="rule"></div>
      <div class="details">Brightmoor Home Loans, Inc – NMLS 40218<br>Marco.Pellam@brightmoorhomeloans.com<br>Office: (555) 014-2291<br>Fax: (555) 014-2292</div>
    </div>
    <a class="btn-small" href="#">VIEW MORE</a>
  </article>

  <article class="member" style="left:612px;top:205px">
    <div class="portrait" role="img" aria-label="Portrait of Dario Vance" style="background:linear-gradient(180deg,#d8dadc,#5a5e64)"></div>
    <div class="info">
      <h3>DARIO VANCE</h3>
      <div class="role">Loan Partner</div>
      <div class="rule"></div>
      <div class="details">Brightmoor Home Loans, Inc – NMLS 40218<br>NMLS ID 173604<br>Dario.Vance@brightmoorhomeloans.com<br>(555) 014-2290</div>
    </div>
    <a class="btn-small" href="#">VIEW MORE</a>
  </article>

  <article class="member" style="left:67px;top:431px">
    <div class="portrait" role="img" aria-label="Portrait of Tomas Rell" style="background:linear-gradient(180deg,#e2e4e6,#5f6670)"></div>
    <div class="info">
      <h3>TOMAS RELL</h3>
      <div class="role">Loan Processor</div>
      <div class="rule"></div>
      <div class="details">NMLS ID 152907<br>Tomas.Rell@brightmoorhomeloans.com<br>(555) 014-2293</div>
    </div>
    <a class="btn-small" href="#">VIEW MORE</a>
  </article>

  <article class="member" style="left:612px;top:431px">
    <div class="portrait" role="img" aria-label="Portrait of Lena Hartwig" style="background:linear-gradient(180deg,#2e3035,#8c7a62)"></div>
    <div class="info">
      <h3>LENA HARTWIG</h3>
      <div class="role">Closing Coordinator/Team Leader</div>
      <div class="rule"></div>
      <div class="details">NMLS 136811<br>Lena.Hartwig@brightmoorhomeloans.com<br>(555) 014-2294</div>
    </div>
    <a class="btn-small" href="#">VIEW MORE</a>
  </article>
</section>

<section class="blog">
  <h2 class="section-title">BLOG</h2>
  <div class="title-rule"></div>
  <div class="card-row blog-row">
    <article class="post">
      <div class="thumb" role="img" aria-label="Couple reviewing paperwork at a kitchen table" style="background:linear-gradient(135deg,#e4d9c8,#8c7660)"></div>
      <h3>SED UT PERSPICIATIS UNDE OMNIS ISTE NATUS ERROR SIT VOLUPTATEM ACCUSANTIUM</h3>
      <p>At vero eos et accusamus et iusto odio dignissimos ducimus qui blanditiis praesentium voluptatum deleniti atque corrupti quos dolores et quas molestias excepturi sint occaecati</p>
      <div class="rule"></div>
      <time>FEBRUARY 12 2018</time>
    </article>
    <article class="post">
      <div class="thumb" role="img" aria-label="Loan officer meeting with clients in an office" style="background:linear-gradient(135deg,#dfe3e6,#7d8690)"></div>
      <h3>UNDE OMNIS ISTE NATUS ERROR SIT VOLUPTATEM ACCUSANTIUM</h3>
      <p>At vero eos et accusamus et iusto odio dignissimos ducimus qui blanditiis praesentium voluptatum deleniti atque corrupti quos dolores et quas molestias excepturi sint occaecati</p>
      <div class="rule"></div>
      <time>FEBRUARY 10 2018</time>
    </article>
    <article class="post">
      <div class="thumb" role="img" aria-label="Couple signing documents with an adviser" style="background:linear-gradient(135deg,#e9e6e1,#8f8272)"></div>
      <h3>PERSPICIATIS UNDE OMNIS ISTE NATUS ERROR SIT VOLUPTATEM ACCUSANTIUM</h3>
      <p>At vero eos et accusamus et iusto odio dignissimos ducimus qui blanditiis praesentium voluptatum deleniti atque corrupti quos dolores et quas molestias excepturi sint occaecati</p>
      <div class="rule"></div>
      <time>FEBRUARY 9 2018</time>
    </article>
  </div>
  <a class="btn btn-outline" href="#">VIEW MORE BLOG</a>
</section>

<footer class="site-footer">
  <div class="footer-brand">
    <span class="brand-mark"></span>
    <div class="brand-name">THE PELLAM TEAM</div>
    <div class="brand-sub">HOME LOAN GROUP</div>
  </div>
  <div class="footer-badges">
    <span class="badge" role="img" aria-label="Equal housing lender badge"></span>
    <span class="partner"><i></i>Brightmoor</span>
  </div>

  <div class="footer-col" style="left:356px">
    <h4>QUICK LINKS</h4>
    <ul><li>HOME</li><li>ABOUT US</li><li>MORTGAGE 101</li><li>CONTACT US</li></ul>
  </div>
  <div class="footer-col" style="left:579px">
    <h4>OTHER LINKS</h4>
    <ul><li>TERMS OF USE</li><li>PRIVACY POLICY</li><li>HELP</li><li>DISCLAIMER</li></ul>
  </div>
  <div class="footer-col resources">
    <h4>RESOURCES</h4>
    <span class="arrows">‹ &nbsp; ›</span>
    <div class="resource"><span>»</span><div>At vero eos et accusamus et iusto odio dignissimos ducimus qui blanditiis praesentium voluptatum<time>FEBRUARY 12th 2018</time></div></div>
    <div class="resource"><span>»</span><div>Deleniti atque corrupti quos dolores et quas molestias excepturi sint occaecati<time>FEBRUARY 8th 2018</time></div></div>
  </div>

  <div class="disclaimer">
    <h4>DISCLAIMER</h4>
    <p>Licensed by the Office of Commerce Stewardship under the Westland Credit Providers Act. Loans made or arranged pursuant to a Westland Credit Providers Act License. Equal Housing Lender Brightmoor Cannot Accept mortgage applications for properties located in New York via this site.</p>
  </div>
  <div class="copyright">© 2018 THE PELLAM TEAM | ALL RIGHTS RESERVED</div>
</footer>

</body>
</html>
```